Medical Practice Business Card

we need a business card for our new medical ophthalmology practice based in Needham Massachusetts. we are looking for a simple , modern and elegant design.
the card needs to contain the following
1- the logo of our practice (please see attached file)
2- the name of the practice : "Silver Birch Retina Care"
3- Doctor's Name: Tobias Rendell MD PhD
4- Specialty: Board-Certified Vitreoretinal Surgeon
5- practice address: 87 Larkspur Ave, Suite 210, Hollisford VT 05481
7- Office number: 617- 482 - 7730
8- fax number: 617- 391 - 2268
9- email: info@sbretinahub.example
10- website: www.sbretinahub.example

```html
<!DOCTYPE html>
<html lang="en">
<head>
<meta charset="utf-8">
<title>Silver Birch Retina Care – Business Card</title>
<link rel="stylesheet" href="https://fonts.googleapis.com/css2?family=Lato:wght@400;700&display=swap">
<style>
  :root {
    --navy: #174a7e;
    --ink: #333a42;
    --muted: #4a5058;
    --paper: #ffffff;
    --backdrop: #e4e6e9;
    --ghost-light: rgba(23, 74, 126, 0.05);
    --ghost-dark: rgba(255, 255, 255, 0.06);
  }
  * { box-sizing: border-box; margin: 0; padding: 0; }
  html, body {
    width: 1200px; height: 1200px; overflow: hidden;
    background: var(--backdrop);
    font-family: "Lato", Arial, sans-serif;
  }
  .canvas { position: relative; width: 1200px; height: 1200px; }

  .card { position: absolute; overflow: hidden; }
  .card-front { left: 217px; top: 32px; width: 777px; height: 448px; background: var(--paper); }
  .card-back  { left: 217px; top: 609px; width: 774px; height: 441px; background: var(--navy); }

  .practice-label {
    position: absolute; left: 35px; top: 59px;
    font-size: 16px; font-weight: 700; letter-spacing: 1.2px;
    color: var(--ink); text-transform: uppercase;
  }

  .brand { position: absolute; display: flex; align-items: center; gap: 12px; font-weight: 700; line-height: 1.1; }
  .brand-mark { border-radius: 50%; border: 3px solid currentColor; flex: none; }
  .brand-name { font-size: 24px; letter-spacing: 0.5px; }

  .brand-front { right: 48px; top: 40px; color: var(--navy); }
  .brand-front .brand-mark { width: 62px; height: 62px; }

  .brand-back { left: 50%; top: 50%; transform: translate(-50%, -50%); color: var(--paper); }
  .brand-back .brand-mark { width: 70px; height: 70px; }
  .brand-back .brand-name { font-size: 27px; }

  .ghost { position: absolute; font-weight: 700; line-height: 1; white-space: nowrap; }
  .ghost-mark { position: absolute; border-radius: 50%; }
  .ghost-front { left: 515px; top: 220px; color: var(--ghost-light); font-size: 70px; }
  .ghost-front .ghost-mark { width: 220px; height: 220px; border: 4px solid var(--ghost-light); left: 0; top: 0; }
  .ghost-front .ghost-text { position: absolute; left: 110px; top: 55px; }
  .ghost-back { left: 40px; top: 30px; color: var(--ghost-dark); font-size: 118px; }
  .ghost-back .ghost-mark { width: 360px; height: 360px; border: 5px solid var(--ghost-dark); left: 0; top: 0; }
  .ghost-back .ghost-text { position: absolute; left: 170px; top: 60px; }

  .doctor { position: absolute; left: 35px; top: 196px; }
  .doctor-name { font-size: 20px; font-weight: 700; color: var(--navy); text-transform: uppercase; letter-spacing: 0.2px; }
  .doctor-credentials { font-size: 13px; font-weight: 400; margin-left: 6px; }
  .doctor-title { margin-top: 6px; font-size: 12.5px; color: var(--muted); }

  .divider { position: absolute; left: 35px; top: 280px; width: 48px; height: 4px; background: var(--navy); }

  .contact-list { position: absolute; left: 35px; top: 302px; list-style: none; }
  .contact-item {
    display: flex; align-items: center; gap: 9px;
    height: 22.5px; font-size: 13.5px; letter-spacing: 1px; color: var(--ink);
  }
  .contact-item.web { letter-spacing: 2px; }
  .contact-item.address { margin-top: 4px; }
  .contact-icon { width: 15px; height: 15px; fill: var(--navy); flex: none; }
</style>
</head>
<body>
<main class="canvas">

  <section class="card card-front" aria-label="Business card front">
    <div class="ghost ghost-front" aria-hidden="true">
      <span class="ghost-mark"></span>
      <span class="ghost-text">Silver<br>Birch</span>
    </div>

    <p class="practice-label">Silver Birch Retina Care</p>

    <div class="brand brand-front">
      <span class="brand-mark"></span>
      <span class="brand-name">Silver Birch<br>Retina Care</span>
    </div>

    <div class="doctor">
      <h1 class="doctor-name">Tobias Rendell<span class="doctor-credentials">[MD PH]</span></h1>
      <p class="doctor-title">Board-Certified Vitreoretinal Surgeon</p>
    </div>

    <span class="divider"></span>

    <ul class="contact-list">
      <li class="contact-item">
        <svg class="contact-icon" viewBox="0 0 24 24"><path d="M6.6 10.8a15.1 15.1 0 0 0 6.6 6.6l2.2-2.2c.3-.3.7-.4 1-.2 1.1.4 2.3.6 3.6.6.6 0 1 .4 1 1V20c0 .6-.4 1-1 1A17 17 0 0 1 3 4c0-.6.4-1 1-1h3.5c.6 0 1 .4 1 1 0 1.3.2 2.5.6 3.6.1.3 0 .7-.2 1z"/></svg>
        617- 482 - 7730
      </li>
      <li class="contact-item">
        <svg class="contact-icon" viewBox="0 0 24 24"><path d="M6 3h12v5H6zM3 9h18v8h-3v4H6v-4H3zm5 6v4h8v-4z"/></svg>
        617- 391 - 2268
      </li>
      <li class="contact-item">
        <svg class="contact-icon" viewBox="0 0 24 24"><path d="M2 5h20v14H2zm2 2v.5l8 5 8-5V7z"/></svg>
        info@sbretinahub.example
      </li>
      <li class="contact-item web">
        <svg class="contact-icon" viewBox="0 0 24 24"><path d="M12 2a10 10 0 1 0 0 20 10 10 0 0 0 0-20zm6.9 6h-3a15 15 0 0 0-1.3-3.9A8 8 0 0 1 18.9 8zM12 4c.9 1.2 1.6 2.5 2 4h-4c.4-1.5 1.1-2.8 2-4zM4.3 14a8 8 0 0 1 0-4h3.4a16 16 0 0 0 0 4zm.8 2h3a15 15 0 0 0 1.3 3.9A8 8 0 0 1 5.1 16zm3-8h-3a8 8 0 0 1 4.3-3.9C8.8 5.3 8.4 6.6 8.1 8zM12 20c-.9-1.2-1.6-2.5-2-4h4c-.4 1.5-1.1 2.8-2 4zm2.3-6H9.7a14 14 0 0 1 0-4h4.6a14 14 0 0 1 0 4zm.3 5.9c.6-1.2 1-2.5 1.3-3.9h3a8 8 0 0 1-4.3 3.9zm1.7-5.9a16 16 0 0 0 0-4h3.4a8 8 0 0 1 0 4z"/></svg>
        www.sbretinahub.example
      </li>
      <li class="contact-item address">
        <svg class="contact-icon" viewBox="0 0 24 24"><path d="M12 2a7 7 0 0 0-7 7c0 5.2 7 13 7 13s7-7.8 7-13a7 7 0 0 0-7-7zm0 9.5a2.5 2.5 0 1 1 0-5 2.5 2.5 0 0 1 0 5z"/></svg>
        87 Larkspur Ave, Suite 210, Hollisford VT 05481
      </li>
    </ul>
  </section>

  <section class="card card-back" aria-label="Business card back">
    <div class="ghost ghost-back" aria-hidden="true">
      <span class="ghost-mark"></span>
      <span class="ghost-text">Silver Birch<br>Retina Care</span>
    </div>
    <div class="brand brand-back">
      <span class="brand-mark"></span>
      <span class="brand-name">Silver Birch<br>Retina Care</span>
    </div>
  </section>

</main>
</body>
</html>
```